Banner ad for Gen Y demographic - Training Institute

We are a training organization that requires two (2) banner ads which we can use to promote our brand, our Diploma of Management and Diploma of Business product offerings, you may visit our website: www.pembertonlearninghub.com.au to grab some background information on us.

I have also included our logo to be used in the banner ad (white or black depending on background color). The text to be used throughout the banner ad is Times New Roman please.

We require flash banners that just have the text changing from one slide to the next. We want something clean and enticing. We also need a call to action button “Start now” or something similar.

I have included the below just as a guide but welcome any creativity that you believe would fit our market. I encourage you to be creative!

Flash panels:
1 Slide – I don’t take classes. I experience them – are you in?
2 Slide - Unlock your potential excellence today

I need two different banner ads / sizes please:

1. 600px (W) x 120px (H), max file size 150KB, gif, jpeg, swf
2. 300px(w) x 250px(h), max size 150KB, gif, jpeg, swf

Out target audience is Gen Y, they are looking for ways to improve their careers, make more money, or to get a different job at their existing employer. They’re looking for a Diploma in Management or Business that will give them the education and the piece of paper that will allow them to get that job.

I look forward to seeing what you come up with!

Industry/Entity Type

Training

```html
<!DOCTYPE html>
<html lang="en">
<head>
<meta charset="utf-8">
<title>Pemberton Learning Hub – Banner Ads</title>
<link rel="stylesheet" href="https://fonts.googleapis.com/css2?family=Advent+Pro:wght@400;500&display=swap">
<style>
  :root {
    --page: #ffffff;
    --amber-deep: #3a1a05;
    --amber-dark: #6b3208;
    --amber-mid: #b0600f;
    --amber-glow: #d98a1e;
    --gold-soft: #e0a54a;
    --ink-light: #ffffff;
    --ink-muted: #f3e2c8;
  }
  * { margin: 0; padding: 0; box-sizing: border-box; }
  html, body {
    width: 1200px; height: 800px; overflow: hidden;
    background: var(--page);
    font-family: "Advent Pro", sans-serif;
  }
  .canvas { position: relative; width: 1200px; height: 800px; }
  .banner {
    position: absolute; left: 200px; width: 800px; height: 160px;
    overflow: hidden; color: var(--ink-light);
  }
  .banner--slide-one { top: 201px; }
  .banner--slide-two { top: 440px; }
  .banner__backdrop {
    position: absolute; inset: 0;
    background:
      radial-gradient(ellipse 180px 90px at 600px 40px, rgba(230,150,40,.75), transparent 70%),
      radial-gradient(ellipse 200px 110px at 330px 90px, rgba(210,140,50,.55), transparent 70%),
      radial-gradient(ellipse 160px 80px at 120px 150px, rgba(90,40,8,.7), transparent 70%),
      radial-gradient(ellipse 120px 120px at 790px 80px, rgba(30,12,3,.85), transparent 70%),
      linear-gradient(90deg, var(--amber-dark) 0%, var(--amber-mid) 30%, var(--amber-glow) 55%, var(--amber-mid) 80%, var(--amber-deep) 100%);
  }
  .brand {
    position: absolute; left: 52px; top: 0; height: 160px;
    display: flex; align-items: center; gap: 14px;
  }
  .brand__mark {
    width: 58px; height: 58px; border-radius: 50%;
    background: var(--ink-light); flex: none;
  }
  .brand__name {
    font-size: 22px; font-weight: 500; line-height: 1; color: var(--ink-light);
    white-space: nowrap;
  }
  .brand__tagline {
    margin-top: 5px; font-size: 12px; font-weight: 400; color: var(--ink-muted);
    white-space: nowrap;
  }
  .banner__divider {
    position: absolute; left: 371px; top: 21px; width: 1.5px; height: 118px;
    background: var(--ink-light);
  }
  .message {
    position: absolute; left: 385px; width: 396px; text-align: center;
  }
  .message__lead { font-size: 22px; font-weight: 400; line-height: 1; white-space: nowrap; }
  .message__question { font-size: 38px; font-weight: 400; line-height: 1; margin-top: 14px; }
  .banner--slide-one .message { top: 40px; }
  .banner--slide-two .message { top: 34px; }
  .cta {
    display: inline-block; margin-top: 18px;
    width: 231px; height: 48px; line-height: 42px;
    border: 3px solid var(--ink-light); border-radius: 10px;
    font-size: 32px; font-weight: 400; letter-spacing: .5px;
    color: var(--ink-light); text-decoration: none;
    background: rgba(90,40,8,.25);
  }
</style>
</head>
<body>
<main class="canvas">

  <section class="banner banner--slide-one">
    <div class="banner__backdrop" role="img" aria-label="Blurred warm amber photograph of a library bookshelf"></div>
    <div class="brand">
      <span class="brand__mark"></span>
      <div>
        <p class="brand__name">Pemberton Learning Hub</p>
        <p class="brand__tagline">Institute of Business and Management</p>
      </div>
    </div>
    <span class="banner__divider"></span>
    <div class="message">
      <p class="message__lead">I don’t take classes. I experience them.</p>
      <p class="message__question">Are you in?</p>
    </div>
  </section>

  <section class="banner banner--slide-two">
    <div class="banner__backdrop" role="img" aria-label="Blurred warm amber photograph of a library bookshelf"></div>
    <div class="brand">
      <span class="brand__mark"></span>
      <div>
        <p class="brand__name">Pemberton Learning Hub</p>
        <p class="brand__tagline">Institute of Business and Management</p>
      </div>
    </div>
    <span class="banner__divider"></span>
    <div class="message">
      <p class="message__lead">Unlock your potential excellence today.</p>
      <a class="cta" href="#">START NOW &gt;&gt;</a>
    </div>
  </section>

</main>
</body>
</html>
```